Mark & Lisa's Hammock Season Party

Invitation to a party 60-80 people at a private residence. Age range 30-40s.

Themes: summer/casual/Australian backyard/local community

**For delivery via both email and printed copy**
Would like one document suitable for both purposes or two versions for electronic or paper invitation. I will arrange printing so please prepare it in a suitable format.

Specimen text attached. Address and phone contact to follow by message with successful bidder

Thanks!
Mark

Target Market(s)

Locals, friends. Party attendees will typicaly be parents in their forties who who be leaving the kids at home for a relaxed party night, and walking home afterward

Industry/Entity Type

Community

Font styles to use
Sans Serif

Requirements
Should not have
• Cliche Australiana imagery. No kangaroos etc

```html
<!DOCTYPE html>
<html lang="en">
<head>
<meta charset="utf-8">
<title>Mark &amp; Lisa's Hammock Season Party – Invitation</title>
<link rel="stylesheet" href="https://fonts.googleapis.com/css2?family=Advent+Pro:wght@600;700&family=Arimo&family=Playfair+Display:wght@700&display=swap">
<style>
  :root {
    --navy: #1c3b53;
    --navy-deep: #15303f;
    --navy-soft: #2a4d66;
    --white: #ffffff;
    --yellow: #f6e116;
    --page: #ffffff;
    --photo-warm: #b89a72;
    --photo-cool: #6f8a8c;
  }
  * { margin: 0; padding: 0; box-sizing: border-box; }
  html, body { width: 1200px; height: 844px; overflow: hidden; background: var(--page); }
  .canvas { position: relative; width: 1200px; height: 844px; }

  .panel {
    position: absolute; top: 0; height: 844px; overflow: hidden;
    background: var(--navy); color: var(--white); text-align: center;
  }
  .panel--front { left: 0; width: 591px; }
  .panel--back { left: 609px; width: 591px; }

  .backdrop {
    position: absolute; inset: 0;
    background: radial-gradient(ellipse at 45% 35%, var(--navy-soft) 0%, var(--navy) 55%, var(--navy-deep) 100%);
  }
  .display { font-family: "Advent Pro", "Arial Narrow", sans-serif; font-weight: 700; text-transform: uppercase; letter-spacing: 0.5px; }

  .headline { position: absolute; left: 0; right: 0; font-size: 60px; line-height: 1; }
  .headline--top { top: 188px; }
  .headline--bottom { top: 410px; }
  .ampersand {
    position: absolute; left: 0; right: 0; top: 258px;
    font-family: "Playfair Display", Georgia, serif; font-size: 128px; line-height: 1;
  }
  .venue { position: absolute; left: 0; right: 0; top: 516px; }
  .venue__at { font-family: "Advent Pro", sans-serif; font-weight: 700; font-size: 42px; line-height: 1; }
  .venue__hosts { font-size: 30px; line-height: 1.15; margin-top: 6px; }
  .venue__event { font-size: 38px; line-height: 1.05; color: var(--yellow); }
  .venue__guests { font-size: 21px; line-height: 1.3; }

  .details {
    position: absolute; left: 0; right: 0; top: 724px;
    font-family: "Arimo", Arial, sans-serif; font-size: 21px; line-height: 34px;
  }

  .hero-photo {
    position: absolute; left: 0; top: 24px; width: 591px; height: 262px;
    background: linear-gradient(120deg, var(--photo-warm) 0%, #d8c59a 40%, var(--photo-cool) 100%);
  }
  .info { position: absolute; left: 0; right: 0; top: 262px; }
  .info__title { font-size: 50px; line-height: 1; }
  .info__list {
    list-style: none; font-family: "Advent Pro", sans-serif; font-weight: 600;
    font-size: 27px; line-height: 31px; margin-top: 4px;
  }
  .info__note {
    font-family: "Advent Pro", sans-serif; font-weight: 600;
    font-size: 27px; line-height: 31px; margin-top: 30px;
  }
  .rsvp {
    position: absolute; left: 0; right: 0; top: 620px; height: 95px;
    background: var(--yellow); color: var(--navy);
    font-family: "Arimo", Arial, sans-serif; font-size: 18px; line-height: 24px;
    display: flex; flex-direction: column; justify-content: center;
  }
</style>
</head>
<body>
<main class="canvas">
  <section class="panel panel--front">
    <div class="backdrop" role="img" aria-label="Tinted photo of smiling friends at a summer party"></div>
    <p class="headline headline--top display">Leave the kids at home</p>
    <p class="ampersand">&amp;</p>
    <p class="headline headline--bottom display">Let your hair down</p>
    <div class="venue">
      <p class="venue__at">at</p>
      <p class="venue__hosts display">Mark &amp; Lisa's</p>
      <p class="venue__event display">Hammock Season Party</p>
      <p class="venue__guests display">for Bellwood Heights and friends</p>
    </div>
    <div class="details">
      <p>Saturday 2 January</p>
      <p>From 6pm ‘til late</p>
      <p>25 Larkspur Street, Bellwood Heights</p>
    </div>
  </section>

  <section class="panel panel--back">
    <div class="backdrop" role="img" aria-label="Tinted photo of friends relaxing together outdoors"></div>
    <div class="hero-photo" role="img" aria-label="Photo of friends raising wine glasses over a shared meal"></div>
    <div class="info">
      <h2 class="info__title display">Child-free event</h2>
      <ul class="info__list">
        <li>Dress: summer casual, bare feet welcome</li>
        <li>Cocktail food provided</li>
        <li>BYO but only if you insist</li>
      </ul>
      <p class="info__note">If you have some friends or neighbours that you like<br>to hang out with,<br>we would love to meet.<br>Bring them with you!</p>
    </div>
    <div class="rsvp">
      <p>An RSVP for catering would be nice.</p>
      <p>Text Mark xxx xxxxxx or Lisa yyyyyyyy before Xmas please.</p>
    </div>
  </section>
</main>
</body>
</html>
```